Tusko Wine Label Design Project

We are creating a wine with a winery in New Hampshire. USA. The bottles need a label Here are some specifics
Brand name Corvel Nox (latin for Wine 22)
Wine: is a blend of Cabernet Sauvignon, Merlot and Shiraz (dominant varietal is cabernet)
Vintage 2023
All ideas from here are thoughts:
Elegant serif or calligraphic script for a sophisticated look. Perhaps Gold foil or embossed for prominence.
Background suggestions: deep Burgandy or matt black for contrast
Illustrations suggestions: Roman inspired wreath (laurel) or column or stylized roman coin.
Tagline suggestion: Timeless
All these graphic elements are just suggestions, you all are the pros. have at it and good luck

```html
<!DOCTYPE html>
<html lang="en">
<head>
<meta charset="utf-8">
<title>Corvel Nox – Cabernet Sauvignon Label</title>
<link rel="stylesheet" href="https://fonts.googleapis.com/css2?family=Cinzel:wght@600&family=Cormorant+Garamond:wght@500&family=Pinyon+Script&family=Arimo&display=swap">
<style>
  :root {
    --page: #ffffff;
    --label-black: #1b1b1b;
    --gold: #c8964a;
    --gold-light: #d9ad5f;
    --body-text: #2a2a2a;
  }
  * { margin: 0; padding: 0; box-sizing: border-box; }
  html, body {
    width: 1200px;
    height: 1200px;
    overflow: hidden;
    background: var(--page);
  }
  .canvas {
    position: relative;
    width: 1200px;
    height: 1200px;
  }
  .label {
    position: absolute;
    left: 376px;
    top: 170px;
    width: 448px;
    height: 670px;
    background: var(--label-black);
  }
  .label-frame {
    position: absolute;
    inset: 0;
  }
  .brand {
    position: absolute;
    top: 150px;
    left: 0;
    width: 100%;
    text-align: center;
  }
  .brand-dot {
    display: block;
    width: 56px;
    height: 56px;
    margin: 0 auto 26px;
    border: 2px solid var(--gold);
    border-radius: 50%;
  }
  .brand-name {
    font-family: "Cinzel", serif;
    font-weight: 600;
    font-size: 46px;
    line-height: 1.1;
    letter-spacing: 2px;
    color: var(--gold);
  }
  .varietal {
    position: absolute;
    top: 381px;
    left: 80px;
    width: 288px;
    height: 51px;
    border-top: 1.5px solid var(--gold);
    border-bottom: 1.5px solid var(--gold);
    display: flex;
    align-items: center;
    justify-content: center;
    font-family: "Cormorant Garamond", serif;
    font-weight: 500;
    font-size: 19px;
    letter-spacing: 2.2px;
    color: var(--gold-light);
  }
  .tagline {
    position: absolute;
    top: 458px;
    left: 0;
    width: 100%;
    display: flex;
    align-items: center;
    justify-content: center;
    gap: 14px;
    font-family: "Pinyon Script", cursive;
    font-size: 34px;
    color: var(--gold);
  }
  .tagline-rule {
    width: 36px;
    height: 1.5px;
    background: var(--gold);
  }
  .seal {
    position: absolute;
    left: 186px;
    top: 528px;
    width: 76px;
    height: 76px;
    border: 2px solid var(--gold);
    border-radius: 50%;
  }
  .description {
    position: absolute;
    left: 160px;
    top: 962px;
    width: 560px;
    text-align: center;
    font-family: "Arimo", sans-serif;
    font-size: 16px;
    line-height: 21px;
    color: var(--body-text);
  }
</style>
</head>
<body>
<main class="canvas">
  <section class="label">
    <svg class="label-frame" width="448" height="670" viewBox="0 0 448 670" aria-hidden="true">
      <path d="M51 34 H397 A24 24 0 0 0 421 58 V612 A24 24 0 0 0 397 636 H51 A24 24 0 0 0 27 612 V58 A24 24 0 0 0 51 34 Z"
            fill="none" stroke="#c8964a" stroke-width="1.6"/>
    </svg>

    <div class="brand">
      <span class="brand-dot"></span>
      <h1 class="brand-name">CORVEL<br>NOX</h1>
    </div>

    <p class="varietal">CABERNET SAUVIGNON</p>

    <p class="tagline">
      <span class="tagline-rule"></span>
      <span class="tagline-text">Timeless</span>
      <span class="tagline-rule"></span>
    </p>

    <div class="seal" aria-hidden="true"></div>
  </section>

  <p class="description">
    Lorem ipsum dolor sit amet, consectetur adipiscing elit, sed do eiusmod tempor incididunt ut labore et dolore magna aliqua. Ut enim ad minim veniam, quis nostrud exercitation ullamco laboris nisi ut aliquip
  </p>
</main>
</body>
</html>
```